Fundraiser Flyer and Email Template

We are looking for a flexible coordinated flyer and email template. The feel of both should be more formal or professional. We are not looking for an overly "political" design that features American flags or other "political" symbols.

We are a political fundraising firm that works with elected officials to set up fundraisers for their campaigns. We send the invites to these events via US Mail and email, so we are looking for a standardized template that will work as both an 8.5 x 11 inch printed flyer, as well as an email template.

The information in the email will be text, but images can be used for formatting.

Some clients have a campaign logo, others do not. The format should be flexible enough to either include the logo, or leave it out. Size also varies.

Any colors in the template should be editable so we can match logos as we get them.

We're open to any format that allows us to edit the format as needed. This would include Photoshop, Microsoft Word, etc.

The text of the invite should include space for:

---------------------------------------
NAME
DISTRICT NUMBER AND OFFICE

DATE OF EVENT
TIME OF EVENT

LOCATION
LOCATION ADDRESS
LOCATION CITY, STATE, ZIP

SUGGESTED CONTRIBUTION LEVELS (Typically 3 levels are provided such as Gold: $1,000, Silver: $500, Bronze: $250)

ADDRESS TO SEND CHECKS TO

RSVP CONTACT INFORMATION

The invite will also need fine-print at the bottom that reads:
"Pennsylvania law allows personal, partnership, and PAC contributions. By law we cannot accept corporate contributions
Paid for by [NAME]"

Industry/Entity Type

It Professional

Font styles to use
Serif
Sans Serif

Requirements
Must have
• Must have spaces for:
• NAME
• DISTRICT NUMBER AND OFFICE
• DATE OF EVENT
• TIME OF EVENT
• LOCATION
• LOCATION ADDRESS
• LOCATION CITY, STATE, ZIP
• SUGGESTED CONTRIBUTION LEVELS (Typically 3 levels are provided such as Gold: $1,000, Silver: $500, Bronze: $250)
• ADDRESS TO SEND CHECKS TO
• RSVP CONTACT INFORMATION
• The invite will also need fine-print at the bottom that reads:
• "Pennsylvania law allows personal, partnership, and PAC contributions. By law we cannot accept corporate contributions
• Paid for by [NAME]"
Should not have
• It should not be overly "political".

```html
<!DOCTYPE html>
<html lang="en">
<head>
<meta charset="utf-8">
<title>Campaign Fundraiser Invitation Flyer</title>
<link rel="stylesheet" href="https://fonts.googleapis.com/css2?family=Montserrat:wght@300;400;600;700;800&family=Roboto+Condensed:wght@400;700&display=swap">
<style>
  :root {
    --red: #e8293a;
    --red-soft: #ef5a64;
    --blue: #0d3382;
    --white: #ffffff;
    --ink: #111111;
    --gold: #f2a51a;
    --silver: #c9ccd4;
    --bronze: #f0591e;
    --backdrop: #e9ecf0;
    --headline: "Montserrat", sans-serif;
    --condensed: "Roboto Condensed", sans-serif;
  }
  * { box-sizing: border-box; margin: 0; padding: 0; }
  html, body { width: 1200px; height: 963px; overflow: hidden; background: var(--backdrop); }
  .canvas { position: relative; width: 1200px; height: 963px; }
  .flyer {
    position: absolute; left: 243px; top: 20px; width: 714px; height: 923px;
    background: var(--white); overflow: hidden;
    box-shadow: 0 10px 30px rgba(0,0,0,.25);
    font-family: var(--headline); color: var(--ink);
  }
  .header-art { position: absolute; left: 0; top: 0; width: 714px; height: 340px; }
  .abs { position: absolute; }
  .center { left: 0; width: 714px; text-align: center; }
  .invite-line { top: 44px; font-size: 28px; font-weight: 300; color: var(--white); letter-spacing: .3px; }
  .invite-line b { font-weight: 700; }
  .title { font-size: 50px; font-weight: 800; color: var(--white); line-height: 1; letter-spacing: 0; }
  .title-1 { top: 86px; }
  .title-2 { top: 140px; }
  .rsvp { left: 42px; top: 223px; color: var(--white); font-family: var(--condensed); }
  .rsvp-label { font-size: 13px; font-weight: 700; }
  .rsvp-phone { font-size: 29px; font-weight: 700; line-height: 1.1; }
  .event-time { right: 38px; top: 235px; color: var(--white); font-family: var(--condensed); text-align: right; }
  .event-date { font-size: 17px; }
  .event-hours { font-size: 20px; font-weight: 700; }
  .field-label { font-size: 15px; font-weight: 600; text-transform: uppercase; }
  .field-box { left: 34px; width: 648px; height: 37px; border: 2px solid var(--ink); }
  .levels-label { left: 36px; top: 625px; font-size: 13px; font-style: italic; font-weight: 600; color: var(--blue); text-transform: uppercase; letter-spacing: -.3px; }
  .tile { top: 648px; height: 93px; background: var(--blue); text-align: center; color: var(--white); padding-top: 13px; }
  .tile-name { font-size: 26px; font-weight: 300; line-height: 1.15; letter-spacing: -.5px; }
  .tile-amount { font-size: 27px; font-weight: 700; line-height: 1.3; }
  .tile-gold { left: 34px; width: 135px; } .tile-gold .tile-name { color: var(--gold); }
  .tile-silver { left: 178px; width: 134px; } .tile-silver .tile-name { color: var(--silver); }
  .tile-bronze { left: 321px; width: 136px; } .tile-bronze .tile-name { color: var(--bronze); }
  .paid-for { left: 463px; top: 648px; width: 219px; height: 93px; border: 2px solid var(--ink); text-align: center; padding-top: 11px; font-size: 12px; }
  .paid-for span { text-decoration: underline; }
  .paid-line { position: absolute; left: 18px; right: 18px; border-top: 1px solid var(--ink); }
  .sponsored { top: 745px; font-size: 12px; }
  .sponsor { top: 772px; width: 46px; height: 46px; border-radius: 50%; background: var(--red); border: 2px solid var(--blue);
    color: var(--white); font-family: var(--condensed); font-size: 10px; line-height: 1.3; text-align: center; padding-top: 8px; }
  .footer { left: 0; top: 837px; width: 714px; height: 86px; background: var(--red); color: var(--white); text-align: center; padding-top: 18px; }
  .footer-web { font-size: 16px; font-weight: 700; }
  .footer-legal { font-size: 11.5px; margin-top: 5px; font-weight: 400; }
</style>
</head>
<body>
<div class="canvas">
  <article class="flyer">
    <svg class="header-art" viewBox="0 0 714 340" aria-hidden="true">
      <polygon fill="var(--red)" points="0,0 714,0 714,134 357,267 0,134"/>
      <polygon fill="var(--blue)" points="0,134 314,261 112,338 0,296"/>
      <polygon fill="var(--blue)" points="714,134 714,296 605,338 400,261"/>
    </svg>
    <div class="abs" role="img" aria-label="Faint star decoration behind the headline"
         style="left:180px;top:0;width:354px;height:267px;background:radial-gradient(ellipse at center, rgba(239,90,100,.55), rgba(232,41,58,0) 70%);"></div>

    <p class="abs center invite-line">YOU ARE <b>INVITED</b> TO A SPECIAL</p>
    <h1 class="abs center title title-1">CAMPAIGN</h1>
    <h1 class="abs center title title-2">FUNDRAISER</h1>

    <div class="abs rsvp">
      <div class="rsvp-label">RSVP CONTACT INFORMATION</div>
      <div class="rsvp-phone">555-010-2468</div>
    </div>
    <div class="abs event-time">
      <div class="event-date">Thursday, August 17, 2017</div>
      <div class="event-hours">5:30 p.m. to 8:30 p.m.</div>
    </div>

    <p class="abs center field-label" style="top:336px;letter-spacing:2px;">Name</p>
    <div class="abs field-box" style="top:356px;"></div>
    <p class="abs center field-label" style="top:411px;">District Number and Office</p>
    <div class="abs field-box" style="top:431px;"></div>
    <p class="abs center field-label" style="top:486px;">Location/Location Address/Location City, State, Zip</p>
    <div class="abs field-box" style="top:506px;"></div>
    <p class="abs center field-label" style="top:562px;">Address to Send Checks To</p>
    <div class="abs field-box" style="top:582px;"></div>

    <p class="abs levels-label">Contribution Levels</p>
    <div class="abs tile tile-gold"><div class="tile-name">GOLD</div><div class="tile-amount">$1,000</div></div>
    <div class="abs tile tile-silver"><div class="tile-name">SILVER</div><div class="tile-amount">$500</div></div>
    <div class="abs tile tile-bronze"><div class="tile-name">BRONZE</div><div class="tile-amount">$250</div></div>
    <div class="abs paid-for">
      <span>Paid for by :</span>
      <div class="paid-line" style="top:57px;"></div>
      <div class="paid-line" style="top:73px;"></div>
    </div>

    <p class="abs center sponsored">Sponsored by:</p>
    <div class="abs sponsor" style="left:47px;">LOGO<br>HERE</div>
    <div class="abs sponsor" style="left:129px;">LOGO<br>HERE</div>
    <div class="abs sponsor" style="left:212px;">LOGO<br>HERE</div>
    <div class="abs sponsor" style="left:294px;">LOGO<br>HERE</div>
    <div class="abs sponsor" style="left:377px;">LOGO<br>HERE</div>
    <div class="abs sponsor" style="left:459px;">LOGO<br>HERE</div>
    <div class="abs sponsor" style="left:542px;">LOGO<br>HERE</div>
    <div class="abs sponsor" style="left:624px;">LOGO<br>HERE</div>

    <footer class="abs footer">
      <div class="footer-web">For more information visit www.campaigninfo-site.com</div>
      <div class="footer-legal">Pennsylvania law allows personal, partnership, and PAC contributions. By law we cannot accept corporate contributions</div>
    </footer>
  </article>
</div>
</body>
</html>
```